Ridgeline Outfitters Business Cards

Recently had a logo done with Artfolio and now looking for a business card to go along with it.

Target Market(s)

Ridgeline Outfitters is a weapons dealer. My market will be primarily men, hunting, shooting type.

Industry/Entity Type

Business

Contact Information for Business Card

I selected double sided, but this is not required, single or double is going to be fine. I picture the logo on one side, or perhaps just the circle which contains "RO" with the remaining info on the other side.

Font styles to use
Sans Serif

Requirements
Must have
• My name: Milo Brandt
• Title: Owner
• tel: 612-555-0187
• web: www.ridgelineoutfittersmn.example
Nice to have
• I like the concept of a black business card. I would like to keep the colors monotone, black, grey, white or red. Red is acceptable because it is in the logo. I have also seen cards that are matte black with shiny black as well, perhaps for the logo (or circle RO) part of the logo.
• I will upload a couple of the logos for use, and also an example I just found of the black on black. and some others that have a nice contrast.
Should not have
• lots of colors are not wanted.

```html
<!DOCTYPE html>
<html lang="en">
<head>
<meta charset="utf-8">
<title>Ridgeline Outfitters Business Cards</title>
<link rel="stylesheet" href="https://fonts.googleapis.com/css2?family=Montserrat:wght@400;600;700&display=swap">
<style>
  :root {
    --backdrop: #2a2422;
    --card-black: #0b0b0b;
    --brand-red: #e3232b;
    --steel-grey: #7d7e80;
    --soft-grey: #9a9b9d;
  }
  * { margin: 0; padding: 0; box-sizing: border-box; }
  html, body {
    width: 1200px;
    height: 1000px;
    overflow: hidden;
    background: var(--backdrop);
    font-family: "Montserrat", sans-serif;
  }
  .canvas { position: relative; width: 1200px; height: 1000px; }
  .card {
    position: absolute;
    width: 540px;
    height: 310px;
    background: var(--card-black);
    box-shadow: 0 6px 18px rgba(0,0,0,0.45);
  }
  .card-front { left: 170px; top: 170px; }
  .card-back  { left: 490px; top: 520px; }

  .brand-lockup {
    position: absolute;
    left: 48px;
    top: 56px;
    display: flex;
    align-items: center;
    gap: 16px;
  }
  .brand-mark { width: 70px; height: 70px; display: block; }
  .brand-name {
    color: var(--brand-red);
    font-weight: 700;
    font-size: 22px;
    letter-spacing: 1px;
    text-transform: uppercase;
  }

  .contact-block {
    position: absolute;
    left: 300px;
    top: 178px;
  }
  .person-name {
    font-weight: 700;
    font-size: 19px;
    letter-spacing: 0.5px;
    color: var(--steel-grey);
    text-transform: uppercase;
  }
  .person-name .surname { color: var(--brand-red); }
  .person-title {
    font-size: 14px;
    color: var(--steel-grey);
    margin-top: 1px;
  }
  .contact-line {
    font-size: 12px;
    color: var(--soft-grey);
    line-height: 1.45;
  }
  .contact-line.first { margin-top: 14px; }

  .back-lockup {
    position: absolute;
    inset: 0;
    display: flex;
    flex-direction: column;
    align-items: center;
    justify-content: center;
    gap: 16px;
  }
  .back-mark { width: 150px; height: 150px; display: block; }
  .back-name {
    color: var(--brand-red);
    font-weight: 700;
    font-size: 20px;
    letter-spacing: 1px;
    text-transform: uppercase;
  }
</style>
</head>
<body>
<main class="canvas">
  <section class="card card-front" aria-label="Business card front">
    <div class="brand-lockup">
      <svg class="brand-mark" viewBox="0 0 70 70" aria-hidden="true">
        <circle cx="35" cy="35" r="31" fill="none" stroke="var(--steel-grey)" stroke-width="5"/>
      </svg>
      <span class="brand-name">Ridgeline Outfitters</span>
    </div>
    <div class="contact-block">
      <p class="person-name">Milo <span class="surname">Brandt</span></p>
      <p class="person-title">owner</p>
      <p class="contact-line first">612-555-0187</p>
      <p class="contact-line">www.ridgelineoutfittersmn.example</p>
    </div>
  </section>

  <section class="card card-back" aria-label="Business card back">
    <div class="back-lockup">
      <svg class="back-mark" viewBox="0 0 150 150" aria-hidden="true">
        <circle cx="75" cy="75" r="68" fill="none" stroke="var(--steel-grey)" stroke-width="9"/>
      </svg>
      <span class="back-name">Ridgeline Outfitters</span>
    </div>
  </section>
</main>
</body>
</html>
```